Business Card Design

We are looking for a business card designed for our landscaping company. We do landscaping installation & Maintenance Services. We would like to see designs that have basic landscaping in background. We also think it is important to have both of our names and phone numbers on the card. We need something that stands out a little whether it is shape of the card or thickness or design.

Industry/Entity Type

Business

Contact Information for Business Card

Pale Ridge Yardworks, paleridgeyardworks@mailbrook.net, Dale Purvine 555-213-7690, Martin Kolbey 555-864-1037

```html
<!DOCTYPE html>
<html lang="en">
<head>
<meta charset="UTF-8">
<title>Pale Ridge Yardworks – Business Card</title>
<link rel="stylesheet" href="https://fonts.googleapis.com/css2?family=Raleway:wght@300;400;700&display=swap">
<style>
  :root {
    --backdrop: #ecebe7;
    --lawn-green: #7dbb47;
    --soil-brown: #5b4936;
    --card-white: #ffffff;
    --rule-white: rgba(255, 255, 255, 0.92);
  }
  * { margin: 0; padding: 0; box-sizing: border-box; }
  html, body {
    width: 848px;
    height: 1200px;
    overflow: hidden;
    background: var(--backdrop);
  }
  body {
    position: relative;
    font-family: "Raleway", sans-serif;
    color: var(--card-white);
  }
  .business-card {
    position: absolute;
    left: 44px;
    top: 383px;
    width: 760px;
    height: 434px;
    background: var(--lawn-green);
    box-shadow: 0 6px 18px rgba(0, 0, 0, 0.12);
    overflow: hidden;
  }
  .horizon-rule {
    position: absolute;
    left: 70px;
    top: 96px;
    width: 620px;
    height: 10px;
  }
  .company-name {
    position: absolute;
    top: 150px;
    left: 0;
    width: 100%;
    text-align: center;
    font-weight: 700;
    font-size: 23px;
    letter-spacing: 5px;
    text-transform: uppercase;
  }
  .contact-list {
    position: absolute;
    top: 226px;
    left: 0;
    width: 100%;
    list-style: none;
    text-align: center;
    font-weight: 400;
    font-size: 22px;
    letter-spacing: 2.4px;
    line-height: 40px;
  }
  .email-band {
    position: absolute;
    left: 0;
    bottom: 0;
    width: 100%;
    height: 78px;
    background: var(--soil-brown);
    display: flex;
    align-items: center;
    justify-content: center;
    font-weight: 400;
    font-size: 22px;
    letter-spacing: 2.2px;
  }
</style>
</head>
<body>
  <section class="business-card" aria-label="Pale Ridge Yardworks business card">
    <svg class="horizon-rule" viewBox="0 0 620 10" aria-hidden="true">
      <line x1="0" y1="5" x2="620" y2="5" stroke="var(--rule-white)" stroke-width="3" stroke-linecap="round"/>
    </svg>
    <h1 class="company-name">Pale Ridge Yardworks</h1>
    <ul class="contact-list">
      <li class="contact-person">Dale Purvine 555-213-7690</li>
      <li class="contact-person">Martin Kolbey 555-864-1037</li>
    </ul>
    <footer class="email-band">paleridgeyardworks@mailbrook.net</footer>
  </section>
</body>
</html>
```